Orlent Telecom Business Card Competition

High quality international communications for consumers and business. We are re-designing our website and re-branding. Our current (old) website can be viewed at www.goorlent-example.net Vision statement - We enable people and communities to build and maintain strong and lasting global connections This is the brand image that we are trying to get across: •Quality—Orlent delivers the highest quality connections wherever you need to communicate. •Service—Orlent is always there for you, with the industry-leading service that promises to ensure that every experience is a good one. •Value—Orlent provides the best value in the global communications market. Typical messaging: Connecting the Most Important People in the World. Focus on international communications

We want to convey our service quality and that we really care about the service we provide and our customers. We want to emphasis the international aspect of our business. We want to make it personal, but it has to relate to business as well as individuals. We want the card to be unique in design but clear enough to read. We want a business prospect as well as a regular person to look at our card and know what we do.

Target Market(s)

Consumer - multi-ethnic consumer base living in the US calling, texting and connecting with family and friends in countries around the world 2. Busine

Industry/Entity Type

Communications

Requirements
Must have
• 1. Logo must be visible (see uploaded)

2.Artist can use variations of our company colors to accent our logo:

Hex Codes:
Magenta = ab3179
Blue = 2895c0
Green = 8ebb3f

3.Must have the following slogan visible: Because Every Voice Carries

below are the required data fields:

Full Name: Mark Tallow
Position: Chief Financial Officer
Office: +1 608-441-2871 ext.318
Mobile: +1 608-441-2871
Fax: +1 608-441-2871
Email: MarkT@goorlent-example.net
URL: www.goorlent-example.net
Address:
71820 Brindle Avenue
suite 412
Larkfield, WI 53719
USA

Nice to have
• Die cut cards or uniquely shaped cards would be interesting to see but not required

```html
<!DOCTYPE html>
<html lang="en">
<head>
<meta charset="utf-8">
<title>Orlent Telecom Business Card</title>
<link rel="stylesheet" href="https://fonts.googleapis.com/css2?family=Sorts+Mill+Goudy&family=Source+Sans+3:wght@400;600&display=swap">
<style>
  :root {
    --magenta: #ab3179;
    --blue: #2895c0;
    --green: #8ebb3f;
    --paper: #ffffff;
    --backdrop: #e9e4dc;
    --rule-blue: #c9dbe4;
    --rule-magenta: #d9b3c8;
  }
  * { box-sizing: border-box; margin: 0; padding: 0; }
  html, body { width: 1200px; height: 675px; overflow: hidden; }
  body {
    background: var(--backdrop);
    font-family: "Source Sans 3", sans-serif;
    position: relative;
  }
  .card {
    position: absolute;
    background: var(--paper);
    box-shadow: 0 3px 10px rgba(0,0,0,.18);
  }
  .card--front { left: 69px; top: 31px; width: 530px; height: 297px; }
  .card--back { left: 506px; top: 331px; width: 573px; height: 307px; }

  .stripes { position: absolute; left: 0; right: 0; }
  .stripes span { display: block; height: 2px; margin-bottom: 2px; }
  .stripes .s-blue { background: var(--blue); height: 3px; }
  .stripes .s-magenta { background: var(--magenta); }
  .stripes .s-green { background: var(--green); }
  .stripes--top { top: 16px; }
  .stripes--bottom { bottom: 14px; }

  .brand-name {
    position: absolute; left: 0; right: 0; text-align: center;
    color: var(--blue); font-weight: 600; letter-spacing: 1px;
  }
  .card--front .brand-name { top: 108px; font-size: 46px; }
  .card--back .brand-name { top: 46px; font-size: 30px; }

  .slogan {
    position: absolute; left: 0; right: 0; top: 224px; text-align: center;
    font-family: "Sorts Mill Goudy", serif; font-size: 19px; color: var(--blue);
  }
  .slogan span { border-bottom: 1px solid var(--rule-blue); padding: 0 4px 3px; }

  .person { position: absolute; left: 62px; top: 148px; color: var(--blue); }
  .person__name { font-size: 25px; font-weight: 400; line-height: 1.2; }
  .person__title { font-size: 12.5px; margin-top: 2px; }

  .contact {
    position: absolute; left: 218px; top: 143px;
    color: var(--green); font-size: 12px; line-height: 16.5px;
    border-collapse: collapse;
  }
  .contact th { text-align: right; font-weight: 400; padding-right: 4px; vertical-align: top; }
  .contact td { text-align: left; }
  .contact .addr th, .contact .addr td { line-height: 14.5px; padding-top: 2px; }

  .web {
    position: absolute; left: 46px; top: 251px;
    display: flex; align-items: center; gap: 7px;
    color: var(--magenta); font-size: 13px; font-weight: 600;
  }
  .web__label { border-bottom: 1px solid var(--rule-magenta); padding-bottom: 1px; }
</style>
</head>
<body>

<section class="card card--front" aria-label="Card front">
  <div class="stripes stripes--top"><span class="s-blue"></span><span class="s-magenta"></span><span class="s-green"></span></div>
  <p class="brand-name">Orlent Telecom</p>
  <p class="slogan"><span>Because Every Voice Carries</span></p>
  <div class="stripes stripes--bottom"><span class="s-blue"></span><span class="s-magenta"></span><span class="s-green"></span></div>
</section>

<section class="card card--back" aria-label="Card back">
  <div class="stripes stripes--top"><span class="s-blue"></span><span class="s-magenta"></span><span class="s-green"></span></div>
  <p class="brand-name">Orlent Telecom</p>

  <div class="person">
    <p class="person__name">Mark Tallow</p>
    <p class="person__title">Chief Financial Officer</p>
  </div>

  <table class="contact">
    <tr><th>Office:</th><td>+1 608-441-2871 ext.318</td></tr>
    <tr><th>Mobile:</th><td>+1 608-441-2871</td></tr>
    <tr><th>Fax:</th><td>+1 608-441-2871</td></tr>
    <tr><th>Email:</th><td>MarkT@goorlent-example.net</td></tr>
    <tr class="addr"><th>Address:</th><td>71820 Brindle Avenue<br>suite 412<br>Larkfield, WI 53719<br>USA</td></tr>
  </table>

  <div class="web">
    <svg width="16" height="15" viewBox="0 0 16 15" aria-hidden="true">
      <rect x="1" y="1" width="14" height="9" rx="1" fill="none" stroke="#ab3179" stroke-width="1.6"/>
      <rect x="7" y="10" width="2" height="3" fill="#ab3179"/>
      <rect x="4" y="13" width="8" height="1.6" fill="#ab3179"/>
    </svg>
    <span class="web__label">www.goorlent-example.net</span>
  </div>

  <div class="stripes stripes--bottom"><span class="s-blue"></span><span class="s-magenta"></span><span class="s-green"></span></div>
</section>

</body>
</html>
```